Reverse Mortgage Postcard-Glen Harlow

Brightfield Lending is the company name We do reverse mortgage and traditional loans as well. This postcard is focusing on reverse mortgages. We would like to have the one image with all the verbiage on one side of the postcard. Then on the other side where the mailing address and stamp goes on one side we would like Glen's picture, the company logo and address with phone numbers, with some verbiage about the company and himself. We will also need some legal information on there at the bottom.
Put his name in Bold, NMLS, Title under his picture and with just His name in Bold BUT if you think it will look better in all bold that's fine. The company address can go at the bottom . Phone number in bold and red with "Call Today for your Free Consultation" bold and black and make it large and where it stands out. Put the phone number underneath it or next to it however you see fit. Phone Number is 855-407-3918 and his direct line is 512-730-4862.

For the small verbiage about Glen please say:
Georgetown residence for over 40 years! I'll beat any reverse mortgage offer because I am local.

Glen Harlow
NMLS#2849103/6418
RMLO/Reverse Mortgage Specialist

Address is:
4173 Pemberton Lane, Ste 260, Georgetown, TX 78628

Industry/Entity Type

It Company

```html
<!DOCTYPE html>
<html lang="en">
<head>
<meta charset="utf-8">
<title>Reverse Mortgage Postcard – Glen Harlow</title>
<link href="https://fonts.googleapis.com/css2?family=Open+Sans:ital,wght@0,400;0,600;0,700;0,800;1,600;1,700&display=swap" rel="stylesheet">
<style>
  :root{
    --stage:#8f8f8f;
    --card:#f4f4f6;
    --paper:#ffffff;
    --blue:#1f8fd8;
    --blue-bright:#3aa7e6;
    --blue-deep:#1a5fa8;
    --navy:#14213d;
    --red:#e01f26;
    --ink:#2a2a2a;
    --grey:#555b63;
    --photo-a:#d9cfc4;
    --photo-b:#eef0f2;
  }
  *{box-sizing:border-box;margin:0;padding:0}
  html,body{width:1200px;height:900px;overflow:hidden}
  body{background:radial-gradient(ellipse at 50% 40%,#b9b9b9,var(--stage));font-family:"Open Sans",Arial,sans-serif;position:relative;color:var(--ink)}

  /* ---------- Mailing side ---------- */
  .mailer{position:absolute;left:30px;top:30px;width:540px;height:360px;background:var(--paper);box-shadow:0 8px 24px rgba(0,0,0,.35);display:flex;overflow:hidden}
  .mailer__agent{width:270px;background:var(--card);position:relative;display:flex;flex-direction:column;align-items:center;padding-top:12px}
  .mailer__mail{flex:1;background:var(--paper)}
  .brand{font-size:15px;font-weight:600;color:var(--navy);letter-spacing:-.2px;line-height:1}
  .brand__tag{font-size:5.5px;font-weight:700;color:var(--blue-deep);margin-top:2px}
  .agent-photo{width:82px;height:78px;margin-top:8px;border:2px solid var(--blue-deep);background:linear-gradient(160deg,var(--photo-a),#8a7a6c)}
  .agent-card{align-self:flex-start;margin-left:66px;margin-top:3px;line-height:1.25}
  .agent-card__name{font-size:8.5px;font-weight:800;font-style:italic;color:var(--ink)}
  .agent-card__title{font-size:5.5px;color:var(--blue);font-weight:600}
  .agent-card__nmls{font-size:6.5px;color:var(--red);font-weight:700}
  .agent-card__direct{font-size:5.5px;font-weight:700;color:var(--ink)}
  .agent-card__direct span{color:var(--red)}
  .pitch{margin-top:12px;text-align:center;font-size:8px;font-weight:600;font-style:italic;color:var(--blue);line-height:1.6}
  .cta{margin-top:8px;font-size:7px;font-weight:700;font-style:italic;color:var(--red)}
  .phone-btn{margin-top:12px;background:var(--blue-bright);color:#fff;font-weight:700;font-size:9px;letter-spacing:.5px;padding:2px 22px;box-shadow:0 2px 3px rgba(0,0,0,.3)}
  .address-bar{position:absolute;left:0;right:0;bottom:0;height:28px;background:var(--navy);display:flex;align-items:center;padding-left:12px;color:#fff;font-size:5.5px;font-weight:600;gap:4px}
  .address-bar__tab{position:absolute;right:0;bottom:0;width:48px;height:34px;background:var(--blue);clip-path:polygon(22% 0,100% 0,100% 100%,0 100%);display:flex;align-items:center;justify-content:center}
  .badge{width:12px;height:12px;border:1.5px solid #fff;margin-left:8px}

  /* ---------- Message side ---------- */
  .faq-card{position:absolute;left:410px;top:398px;width:760px;height:480px;background:var(--card);box-shadow:0 10px 28px rgba(0,0,0,.4);overflow:hidden}
  .faq-card__wave{position:absolute;left:0;bottom:0;width:760px;height:150px}
  .faq-card__photo{position:absolute;left:0;top:150px;width:210px;height:210px;background:linear-gradient(135deg,var(--photo-b),var(--photo-a))}
  .hero{position:absolute;left:18px;top:16px;width:200px}
  .hero__title{font-size:17px;font-weight:700;color:var(--blue);line-height:1.05;text-transform:uppercase}
  .hero__intro{font-size:9px;color:var(--grey);margin-top:8px;line-height:1.3}
  .faq-cols{position:absolute;left:225px;top:16px;right:14px;display:flex;gap:12px}
  .faq-col{flex:1}
  .faq-col--lead{position:absolute;left:-8px;top:130px;width:0}
  .q{font-size:7px;font-weight:700;color:var(--blue);text-transform:uppercase;line-height:1.15;margin-top:9px}
  .q:first-child{margin-top:0}
  .a{font-size:7.2px;color:var(--grey);line-height:1.3;margin-top:2px}
  .a ul{list-style:none;margin-top:2px}
  .a li::before{content:"• "}
  .lead-qa{position:absolute;left:222px;top:236px;width:108px}
</style>
</head>
<body>

<section class="mailer" aria-label="Postcard mailing side">
  <div class="mailer__agent">
    <div class="brand">Brightfield Lending</div>
    <div class="brand__tag">Home Loans Made Simple</div>
    <div class="agent-photo" role="img" aria-label="Portrait photo of Glen Harlow"></div>
    <div class="agent-card">
      <div class="agent-card__name">Glen Harlow / RMLO</div>
      <div class="agent-card__title">Reverse Mortgage Specialist</div>
      <div class="agent-card__nmls">NMLS#2849103/6418</div>
      <div class="agent-card__direct">Direct line: <span>512-730-4862</span></div>
    </div>
    <p class="pitch">Georgetown residence for over 40 years!<br>I'll beat any reverse mortgage offer<br>because I am local.</p>
    <p class="cta">"Call Today for your Free Consultation"</p>
    <div class="phone-btn">855-407-3918</div>
    <div class="address-bar">
      <svg width="7" height="9" viewBox="0 0 10 14" aria-hidden="true"><path d="M5 0a5 5 0 0 0-5 5c0 4 5 9 5 9s5-5 5-9a5 5 0 0 0-5-5zm0 7a2 2 0 1 1 0-4 2 2 0 0 1 0 4z" fill="#fff"/></svg>
      4173 Pemberton Lane, Ste 260, Georgetown, TX 78628
      <div class="address-bar__tab"><div class="badge"></div></div>
    </div>
  </div>
  <div class="mailer__mail"></div>
</section>

<section class="faq-card" aria-label="Postcard message side">
  <div class="faq-card__photo" role="img" aria-label="Photo of a smiling retired couple reviewing papers at home"></div>
  <svg class="faq-card__wave" viewBox="0 0 760 150" preserveAspectRatio="none" aria-hidden="true">
    <path d="M0 70 C200 140 420 120 760 40 L760 150 L0 150Z" fill="#bfe3f6"/>
    <path d="M0 95 C220 150 450 130 760 70 L760 150 L0 150Z" fill="#6cc0ec"/>
    <path d="M0 60 C210 130 430 115 760 30 L760 40 C430 125 210 140 0 72Z" fill="#1a5fa8"/>
    <path d="M0 120 C230 160 470 140 760 100 L760 150 L0 150Z" fill="#3aa7e6"/>
  </svg>

  <div class="hero">
    <h1 class="hero__title">Enjoy your<br>retirement on<br>your terms.</h1>
    <p class="hero__intro">Get answers to common questions and find out if a reverse mortgage is the right choice for you.</p>
  </div>

  <div class="lead-qa">
    <p class="q">Will the bank own my home?</p>
    <p class="a">The bank does not take ownership of your home, they simply extend a loan to you. You continue to own and live in your home and are responsible for payment of property taxes, required insurance and any applicable HOA fees.</p>
  </div>

  <div class="faq-cols" style="left:340px">
    <div class="faq-col">
      <p class="q">It sounds too good to be true. How does this work?</p>
      <p class="a">There are many misconceptions about reverse mortgages, so it is important to know the facts. A reverse mortgage, or HECM (Home Equity Conversion Mortgage) is a federally insured loan that allows you to tap into the equity you have built up in your home.</p>
      <p class="q">If I have an existing mortgage, can I get a reverse mortgage?</p>
      <p class="a">Yes. Many borrowers use a reverse mortgage to pay off their existing mortgage and eliminate their monthly mortgage payment. In many cases, there is a line of credit left over for the borrower.</p>
    </div>
    <div class="faq-col">
      <p class="q">Do my children/family members lose their inheritance?</p>
      <p class="a">No. A borrower may designate an heir of their choosing. The heir(s) will inherit the home after the last surviving borrower passes away and may then choose to keep (by paying off the amount of reverse mortgage balance) or sell the home. Should they choose to sell, any remaining equity after paying off the loan (minus interest and/or fees) would be theirs.</p>
      <p class="q">How much do I qualify for?</p>
      <p class="a">The amount you can borrow is dependent on several factors including: age, home appraisal value and current interest rates.</p>
      <p class="q">Do I need to be suffering a financial hardship to qualify?</p>
      <p class="a">No. It is another common misconception that reverse mortgages are only available to those who are struggling financially. In fact, many affluent borrowers who work with financial planners are using this as a tool to better their quality of life during retirement.</p>
    </div>
    <div class="faq-col">
      <p class="q">Will a reverse mortgage affect my Social Security or Medicare benefits?</p>
      <p class="a">You should always check with your tax specialist before applying, however, in general a reverse mortgage does not affect Social Security and/or Medicare.</p>
      <p class="q">Are there any restrictions on how I can spend my loan proceeds?</p>
      <p class="a">There are no restrictions once any existing mortgages or liens are paid off. Many reverse mortgage borrowers use their cash payments to delay their Social Security payments, pay medical bills, travel or simply supplement their retirement income.</p>
    </div>
    <div class="faq-col">
      <p class="q">What paperwork will I need to have ready?</p>
      <div class="a">Your loan officer will walk you through each step, however you should have the below documents available when you begin your application:
        <ul>
          <li>Proof of Social Security number</li>
          <li>Proof of income</li>
          <li>Proof of age (driver's license, birth certificate, etc.)</li>
          <li>Photo ID (driver's license, passport or state-issued ID)</li>
          <li>Required homeowners insurance policy(ies)</li>
          <li>Copy of mortgage statement (if applicable)</li>
        </ul>
      </div>
    </div>
  </div>
</section>

</body>
</html>
```